【 概要 】 当社は、ペットフード商品を取り扱っております。 引き続き、犬用のおやつジャーキー商品ラベルデザインをお願いいたします。 作成物:犬のおやつで内容は、「鮭を使用した完全無添加、ヒューマングレードのジャーキー」です。 【 依頼詳細 】 ■詳細は、添付のエクセルデータに記載しております。 商品名:「北海道産 カリッと鶏ささみ棒(スライスタイプ)」です。 ■イメージ:エクセルデータにイメージを記載しています。 ※鮭の和と高級なイメージの中で親しみが出るようなソフトな雰囲気を意識していただきたいです。愛犬のおやつなので。 愛犬に安心安全で高級なおやつをあげたいと思いたくなるようなデザインを望んでいます。 ■ターゲット:愛犬に安心安全で高級なおやつをあげたいと思ってくれる飼い主様 【お願い】 採用となった方に修正などのご協力をお願いする場合がありますのでご了承ください。 ※デザインのイメージや柔軟なご対応にご協力いただけた場合、当社でも今後もデザインのご依頼を定期的にさせていただきたいと考えております。 ・編集可能なファイル形式(ai) ・PDFデータ ・フォトショップ(.psd) ・高解像度JPG形式(JPG) 【 契約金額(税込) 】 33,000円(税込) ※契約金額(税込)からシステム利用料を差し引いた金額が、ワーカーさまの受取金額となります ・採用されたデザインの著作権は弊社に譲渡いただき、同意いただいた上でご応募ください。 ■禁止事項 ------------------ ・他で登録されているデザインや転用など、他社の知的財産権を侵すこと ・他のクライアントへ既に提案した内容の転用など -------------------------------- 採用された方は継続的に仕事を依頼する場合もあります。 末永くお付き合いできるデザイナー様を探しております。 素敵なデザインに仕上げるために、ぜひお力をお貸しください その他ご質問等ありましたら、気軽にお問い合わせください。 ご応募をお待ちしております! |
こちらの作品が、当社としてもブランドのイメージに合ったデザインでした。ワーカー様もご対応が丁寧な方で好感をもてました。
皆様、素敵なデザインをご提案いただきありがとうございました。こんなにもご応募いただけたこと、うれしく存じます。また、機会があればご依頼させていただきますのでよろしくお願いいたします。

```html
<!DOCTYPE html>
<html lang="ja">
<head>
<meta charset="utf-8">
<title>カリッと鶏ささみ棒 ラベル</title>
<link href="https://fonts.googleapis.com/css2?family=Yuji+Syuku&family=Zen+Old+Mincho:wght@500;700&display=swap" rel="stylesheet">
<style>
  :root {
    --backdrop: #ebe6dc;
    --paper: #f5f1e5;
    --paper-edge: #e4dcc8;
    --ink: #1e1e1e;
    --navy: #2e4a68;
    --navy-soft: #3f5f80;
    --fish-blue: #7d9fb8;
    --fish-light: #c9d8e2;
    --gold: #c9a55a;
    --dog-tone: #d8b98c;
    --dog-grey: #a9acb0;
  }
  html, body {
    margin: 0;
    width: 1200px;
    height: 1200px;
    overflow: hidden;
    background: var(--backdrop);
  }
  .label {
    position: absolute;
    left: 250px;
    top: 145px;
    width: 700px;
    height: 910px;
    background:
      radial-gradient(circle at 20% 30%, rgba(201,165,90,.18) 0 3px, transparent 4px),
      radial-gradient(circle at 70% 15%, rgba(201,165,90,.22) 0 2px, transparent 3px),
      radial-gradient(circle at 85% 62%, rgba(201,165,90,.2) 0 3px, transparent 4px),
      radial-gradient(circle at 12% 75%, rgba(201,165,90,.2) 0 2px, transparent 3px),
      radial-gradient(circle at 55% 88%, rgba(201,165,90,.18) 0 3px, transparent 4px),
      var(--paper);
    box-shadow: inset 0 0 0 2px var(--paper-edge);
    overflow: hidden;
    font-family: "Zen Old Mincho", serif;
    color: var(--ink);
  }
  .label-frame {
    position: absolute;
    inset: 18px;
    border: 1.5px solid rgba(46,74,104,.35);
  }
  .name-lead {
    position: absolute;
    left: 90px;
    top: 60px;
    font-family: "Yuji Syuku", serif;
    font-size: 66px;
    letter-spacing: 2px;
    transform: rotate(-6deg);
    transform-origin: left center;
  }
  .name-main {
    position: absolute;
    left: 60px;
    top: 170px;
    font-family: "Yuji Syuku", serif;
    font-size: 100px;
    line-height: 1;
    letter-spacing: -2px;
  }
  .name-tail {
    position: absolute;
    left: 300px;
    top: 320px;
    font-family: "Yuji Syuku", serif;
    font-size: 84px;
    line-height: 1;
  }
  .origin-tag {
    position: absolute;
    left: 480px;
    top: 52px;
    width: 150px;
    height: 380px;
    background: rgba(46,74,104,.08);
    border: 2px solid var(--navy);
    display: flex;
    flex-direction: column;
    align-items: center;
    padding-top: 18px;
    box-sizing: border-box;
  }
  .origin-map {
    width: 78px;
    height: 62px;
    background: var(--navy);
    border-radius: 6px;
  }
  .origin-text {
    margin-top: 18px;
    writing-mode: vertical-rl;
    font-family: "Yuji Syuku", serif;
    font-size: 62px;
    color: var(--navy);
    letter-spacing: 4px;
  }
  .fish-art {
    position: absolute;
    left: 220px;
    top: 400px;
    width: 460px;
    height: 280px;
    background: linear-gradient(150deg, var(--fish-light), var(--fish-blue) 60%, var(--navy-soft));
    border-radius: 50% 40% 50% 45% / 55% 45% 55% 45%;
    transform: rotate(-28deg);
    opacity: .85;
  }
  .type-badge {
    position: absolute;
    left: 160px;
    top: 490px;
    width: 180px;
    height: 180px;
    border-radius: 50%;
    background: var(--navy);
    color: var(--paper);
    display: flex;
    flex-direction: column;
    align-items: center;
    justify-content: center;
    font-size: 34px;
    font-weight: 700;
    line-height: 1.3;
    box-shadow: 0 0 0 6px var(--paper), 0 0 0 8px var(--navy);
  }
  .category {
    position: absolute;
    left: 0;
    right: 0;
    top: 720px;
    text-align: center;
    font-size: 38px;
    font-weight: 500;
    letter-spacing: 4px;
  }
  .dogs-art {
    position: absolute;
    left: 40px;
    right: 40px;
    bottom: 0;
    height: 120px;
    background: linear-gradient(90deg, var(--dog-tone), var(--dog-grey) 35%, #efe8da 55%, var(--dog-tone) 80%, #e7c79a);
    border-radius: 60px 60px 0 0;
    opacity: .9;
  }
</style>
</head>
<body>
  <main class="label">
    <div class="label-frame"></div>

    <div class="fish-art" role="img" aria-label="和風タッチの魚のイラスト"></div>

    <div class="name-lead">カリッと</div>
    <div class="name-main">鶏ささみ</div>
    <div class="name-tail">棒</div>

    <div class="origin-tag">
      <div class="origin-map" role="img" aria-label="北海道の地図"></div>
      <div class="origin-text">北海道産</div>
    </div>

    <div class="type-badge"><span>スライス</span><span>タイプ</span></div>

    <div class="category">犬のおやつ</div>

    <div class="dogs-art" role="img" aria-label="並んで座る犬たちのイラスト"></div>
  </main>
</body>
</html>
```